Word Page Templates x 5

1 x Letterhead Template with Header and Footer able to be printed to paper and pdf with non blurry resolution
- File attached looks ok on computer screen but does not print the same
- We are wanting it to print like it looks on the screen
- We are wanting it to print not fuzzy in resolution
- We are wanting the banner to be on the absolute edge of the page like it is on the computer screen
- We are needing to print this to paper and pdf with perfect resolution and colour

Please can someone help us!!

I have provided the logo files in our posession. If better resolutions are required please let us know.

We are also wanting 4 simple page templates to be setup in Landscape and Portrait orientation as well once we are happy with the letterhead that is provided samples have been provided
Updates

Hi all I have the vector files available now along with a Colour profile

Requirements
Must have
• Clear when printed on A4 Paper
Should not have
• Blurry images, Colour must be correct (same as Logo) - Please reference our website if need be ..... vornal.com.au

```html
<!DOCTYPE html>
<html lang="en">
<head>
<meta charset="utf-8">
<title>Vornal Pavement Services – Letterhead Concepts</title>
<link href="https://fonts.googleapis.com/css2?family=Roboto:wght@300;400;700&display=swap" rel="stylesheet">
<style>
:root{
  --green:#12853f;
  --navy:#23407a;
  --grey:#8c8e90;
  --grey-light:#b4b6b8;
  --ink:#3b3b3b;
  --paper:#ffffff;
  --canvas:#ffffff;
}
*{box-sizing:border-box;margin:0;padding:0}
html,body{width:1200px;height:1200px;overflow:hidden;background:var(--canvas)}
body{position:relative;font-family:"Roboto",Arial,sans-serif;color:var(--ink)}
.sheet{position:absolute;width:358px;height:507px;background:var(--paper);box-shadow:0 1px 4px rgba(0,0,0,.18);overflow:hidden}
.sheet--side-left{left:238px;top:132px}
.sheet--side-right{left:627px;top:132px}
.sheet--column{left:38px;top:664px}
.sheet--bands-footer{left:423px;top:662px}
.sheet--bands{left:808px;top:662px}

.wordmark{position:absolute;line-height:1}
.wordmark__name{display:block;font-weight:700;font-size:27px;letter-spacing:1px;color:var(--green)}
.wordmark__tag{display:block;font-weight:700;font-size:6px;letter-spacing:.8px;color:var(--grey);text-align:right;margin-top:2px}
.wordmark--small .wordmark__name{font-size:15px;color:var(--grey)}
.wordmark--small .wordmark__tag{font-size:3.4px;margin-top:1px}

.contact{position:absolute;font-size:4.8px;line-height:8px;color:#6d6f71;font-weight:300}
.contact b{font-weight:700}
.contact--light{color:#fff}

.letter{position:absolute;font-size:6.8px;line-height:14.5px;font-weight:300;color:var(--ink)}
.letter p{margin-bottom:14.5px}
.letter .sign-off{text-align:right}

.badge-stack{position:absolute;display:flex;flex-direction:column;align-items:center}
.badge{background:var(--grey-light)}
.badge--round{width:22px;height:18px;border-radius:50%}
.badge--square{width:22px;height:22px;border-radius:3px}
.badge--wide{width:40px;height:14px;border-radius:7px}

.affiliation{position:absolute;font-size:4.6px;letter-spacing:.9px;color:var(--grey);font-weight:400;white-space:nowrap}
.affiliation--up{writing-mode:vertical-rl;transform:rotate(180deg)}
.affiliation--down{writing-mode:vertical-rl;color:#fff}

.strip{position:absolute}
.band{position:absolute;left:0;width:100%;height:21px;background:linear-gradient(90deg,var(--green),var(--navy))}
.rule{position:absolute;width:18px;height:3px;background:#fff}
</style>
</head>
<body>

<!-- Concept 1: grey left strip -->
<section class="sheet sheet--side-left">
  <div class="strip" role="img" aria-label="Textured grey pavement pattern strip" style="left:0;top:0;width:17px;height:507px;background:linear-gradient(180deg,#8d8f91,#a3a5a7)"></div>
  <svg class="strip" style="left:0;top:0" width="37" height="507" viewBox="0 0 37 507">
    <polygon points="17,0 37,0 37,60 17,88" fill="var(--grey)"/>
    <polygon points="17,88 37,56 37,95 17,125" fill="var(--green)"/>
    <polygon points="17,125 37,95 37,112 17,142" fill="var(--navy)"/>
    <polygon points="17,142 37,112 37,125 17,150" fill="var(--grey)"/>
  </svg>
  <div class="affiliation affiliation--up" style="left:5px;top:282px;color:#fff">VORNAL PAVEMENT SERVICES ARE PROUDLY AFFILIATED:</div>
  <div class="wordmark" style="left:56px;top:22px"><span class="wordmark__name">VORNAL</span><span class="wordmark__tag">PAVEMENT SERVICES</span></div>
  <div class="contact" style="left:267px;top:23px"><b>A.</b> PO Box 2183,<br>Kestrel Bay QLD 4390<br><b>P.</b> 07 5550 1234<br><b>E.</b> admin@vornal.com.au<br><b>W.</b> vornal.com.au</div>
  <div class="badge-stack" style="left:28px;top:308px;gap:28px">
    <span class="badge badge--round" role="img" aria-label="Partner badge"></span>
    <span class="badge badge--square" role="img" aria-label="Member badge"></span>
    <span class="badge badge--square" role="img" aria-label="Airports association badge"></span>
    <span class="badge badge--wide" role="img" aria-label="Partner badge"></span>
  </div>
  <div class="letter" style="left:90px;top:105px;width:238px">
    <p>Dear Mrs Halloway,</p>
    <p>The quick, brown fox jumps over a lazy dog. DJs flock by when KTV ax quiz prog. Junk KTV quiz graced by fox whelps. Bawds jog, flick quartz, vex nymphs. Waltz, bad nymph, for quick jigs vex!</p>
    <p>Fox nymphs grab quick-jived waltz. Brick quiz whangs jumpy veldt fox. Bright vixens jump; dozy fowl quack. Quick wafting zephyrs vex bold Jim. Quick zephyrs blow, vexing daft Jim. Fur-clad fop blew my junk TV quiz. How quickly daft jumping zebras vex. Two driven jocks help fax my big quiz. Quick, Baz, get my woven flax jodhpurs! "Now fax quiz Jack!" my brave ghost pled.</p>
    <p>Five quacking zephyrs jolt my wax bed. Flummoxed by job, kvetching W. zaps Iraq. Cozy sphinx waves quart jug of bad milk. A very bad quack might jinx zippy fowls. Few quips galvanized the mock jury box. Quick brown dogs jump over the lazy fox. The jay, pig, fox, zebra, and my wolves quack! Blowzy red vixens fight for a quick jump. Jorund Felwick was gazed by KTV for luck. A wizard's job is to vex chumps quickly in fog. Watch "Quizzard!", Rex Talbot's fun TV quiz game. Woven silk pyjamas exchanged for blue quartz.</p>
    <p class="sign-off">Best Regards,</p>
  </div>
</section>

<!-- Concept 2: grey right strip -->
<section class="sheet sheet--side-right">
  <svg class="strip" style="left:322px;top:0" width="36" height="507" viewBox="0 0 36 507">
    <path d="M0,0 H36 V507 H19 V124 C19,112 0,105 0,90 Z" fill="var(--grey)"/>
    <path d="M0,62 C0,72 19,78 19,90 V124 C19,112 0,105 0,90 Z" fill="var(--green)"/>
    <path d="M0,80 C0,92 19,98 19,108 V124 C19,112 0,106 0,100 Z" fill="var(--navy)"/>
  </svg>
  <div class="affiliation affiliation--down" style="left:341px;top:332px">VORNAL PAVEMENT SERVICES ARE PROUDLY AFFILIATED:</div>
  <div class="wordmark" style="left:22px;top:22px"><span class="wordmark__name">VORNAL</span><span class="wordmark__tag">PAVEMENT SERVICES</span></div>
  <div class="letter" style="left:52px;top:82px;width:196px">
    <p>Dear Mrs Halloway,</p>
    <p>The quick, brown fox jumps over a lazy dog. DJs flock by when KTV ax quiz prog. Junk KTV quiz graced by fox whelps. Bawds jog, flick quartz, vex nymphs. Waltz, bad nymph, for quick jigs vex!</p>
    <p>Fox nymphs grab quick-jived waltz. Brick quiz whangs jumpy veldt fox. Bright vixens jump; dozy fowl quack. Quick wafting zephyrs vex bold Jim. Quick zephyrs blow, vexing quickly daft jumping zebras vex. Two driven jocks help fax my big quiz. Quick, Baz, get my woven flax jodhpurs! "Now fax quiz Jack!" my brave ghost pled.</p>
    <p>Five quacking zephyrs jolt my wax bed. Flummoxed by job, kvetching W. zaps Iraq. Cozy sphinx waves quart jug of bad galvanized the mock jury box. Quick brown dogs jump over the lazy fox. The jay, pig, fox, zebra, and my wolves quack! was gazed by KTV for luck. A wizard's job is to vex chumps quickly in fog. Watch "Quizzard!", Rex Talbot's fun TV quiz game. Woven silk pyjamas exchanged for blue quartz.</p>
    <p class="sign-off">Best Regards,</p>
  </div>
  <div class="wordmark wordmark--small" style="left:22px;top:421px"><span class="wordmark__name">VORNAL</span><span class="wordmark__tag">PAVEMENT SERVICES</span></div>
  <div class="contact" style="left:22px;top:446px"><b>A.</b> PO Box 2183,<br>Kestrel Bay QLD 4390<br><b>P.</b> 07 5550 1234<br><b>E.</b> admin@vornal.com.au<br><b>W.</b> vornal.com.au</div>
  <div class="badge-stack" style="left:296px;top:345px;gap:22px">
    <span class="badge badge--round" role="img" aria-label="Partner badge"></span>
    <span class="badge badge--square" role="img" aria-label="Member badge"></span>
    <span class="badge badge--square" role="img" aria-label="Airports association badge"></span>
    <span class="badge badge--wide" style="width:34px" role="img" aria-label="Partner badge"></span>
  </div>
</section>

<!-- Concept 3: gradient column -->
<section class="sheet sheet--column">
  <div class="strip" style="left:0;top:0;width:79px;height:507px;background:linear-gradient(180deg,#1c3f72 0%,#0b5a6a 50%,#17813f 100%)"></div>
  <span class="rule" style="left:10px;top:46px"></span>
  <div class="contact contact--light" style="left:10px;top:56px"><b>A.</b> PO Box 2183,<br>Kestrel Bay QLD 4390<br><b>P.</b> 07 5550 1234<br><b>E.</b> admin@vornal.com.au<br><b>W.</b> vornal.com.au</div>
  <span class="rule" style="left:10px;top:243px"></span>
  <div class="contact contact--light" style="left:10px;top:252px;font-size:5.2px;letter-spacing:.8px;line-height:8.2px">VORNAL<br>PAVEMENT<br>SERVICES ARE<br>PROUDLY<br>AFFILIATED:</div>
  <div class="badge-stack" style="left:18px;top:314px;gap:26px">
    <span class="badge badge--round" style="background:#d8e4e0" role="img" aria-label="Partner badge"></span>
    <span class="badge badge--square" style="background:#d8e4e0" role="img" aria-label="Member badge"></span>
    <span class="badge badge--square" style="background:#d8e4e0" role="img" aria-label="Airports association badge"></span>
    <span class="badge badge--wide" style="background:#d8e4e0" role="img" aria-label="Partner badge"></span>
  </div>
  <div class="wordmark" style="left:233px;top:22px"><span class="wordmark__name">VORNAL</span><span class="wordmark__tag">PAVEMENT SERVICES</span></div>
  <div class="letter" style="left:104px;top:101px;width:238px">
    <p>Dear Mrs Halloway,</p>
    <p>The quick, brown fox jumps over a lazy dog. DJs flock by when KTV ax quiz prog. Junk KTV quiz graced by fox whelps. Bawds jog, flick quartz, vex nymphs. Waltz, bad nymph, for quick jigs vex!</p>
    <p>Fox nymphs grab quick-jived waltz. Brick quiz whangs jumpy veldt fox. Bright vixens jump; dozy fowl quack. Quick wafting zephyrs vex bold Jim. Quick zephyrs blow, vexing daft Jim. Fur-clad fop blew my junk TV quiz. How quickly daft jumping zebras vex. Two driven jocks help fax my big quiz. Quick, Baz, get my woven flax jodhpurs! "Now fax quiz Jack!" my brave ghost pled.</p>
    <p>Five quacking zephyrs jolt my wax bed. Flummoxed by job, kvetching W. zaps Iraq. Cozy sphinx waves quart jug of bad milk. A very bad quack might jinx zippy fowls. Few quips galvanized the mock jury box. Quick brown dogs jump over the lazy fox. The jay, pig, fox, zebra, and my wolves quack! Blowzy red vixens fight for a quick jump. Jorund Felwick was gazed by KTV for luck. A wizard's job is to vex chumps quickly in fog. Watch "Quizzard!", Rex Talbot's fun TV quiz game. Woven silk pyjamas exchanged for blue quartz.</p>
    <p class="sign-off">Best Regards,</p>
  </div>
</section>

<!-- Concept 4: gradient bands with footer -->
<section class="sheet sheet--bands-footer">
  <div class="band" style="top:0" role="img" aria-label="Green to blue chevron road-marking band"></div>
  <div class="wordmark" style="left:21px;top:39px"><span class="wordmark__name">VORNAL</span><span class="wordmark__tag">PAVEMENT SERVICES</span></div>
  <div class="letter" style="left:49px;top:86px;width:282px">
    <p>Dear Mrs Halloway,</p>
    <p>The quick, brown fox jumps over a lazy dog. DJs flock by when KTV ax quiz prog. Junk KTV quiz graced by fox whelps. Bawds jog, flick quartz, vex nymphs. Waltz, bad nymph, for quick jigs vex!</p>
    <p>Fox nymphs grab quick-jived waltz. Brick quiz whangs jumpy veldt fox. Bright vixens jump; dozy fowl quack. Quick wafting zephyrs vex bold Jim. Quick zephyrs blow, vexing daft Jim. Fur-clad fop blew my junk TV quiz. How quickly daft jumping zebras vex. Two driven jocks help fax my big quiz. Quick, Baz, get my woven flax jodhpurs! "Now fax quiz Jack!" my brave ghost pled.</p>
    <p>Five quacking zephyrs jolt my wax bed. Flummoxed by job, kvetching W. zaps Iraq. Cozy sphinx waves quart jug of bad milk. A very bad quack might jinx zippy fowls. Few quips galvanized the mock jury box. Quick brown dogs jump over the lazy fox. The jay, pig, fox, zebra, and my wolves quack! Blowzy red vixens fight for a quick jump. Jorund Felwick was gazed by KTV for luck. A wizard's job is to vex chumps quickly in fog. Watch "Quizzard!", Rex Talbot's fun TV quiz game. Woven silk pyjamas exchanged for blue quartz.</p>
    <p>Best Regards,</p>
  </div>
  <div class="affiliation" style="left:21px;top:431px;line-height:6px">VORNAL PAVEMENT SERVICES ARE<br>PROUDLY AFFILIATED:</div>
  <div style="position:absolute;left:21px;top:453px;display:flex;gap:14px;align-items:flex-end">
    <span class="badge badge--wide" style="width:34px;height:12px" role="img" aria-label="Partner badge"></span>
    <span class="badge badge--square" style="width:18px;height:20px" role="img" aria-label="Airports association badge"></span>
    <span class="badge badge--round" style="width:20px;height:15px" role="img" aria-label="Partner badge"></span>
    <span class="badge badge--square" style="width:20px;height:22px" role="img" aria-label="Member badge"></span>
  </div>
  <div class="wordmark wordmark--small" style="left:270px;top:412px"><span class="wordmark__name">VORNAL</span><span class="wordmark__tag">PAVEMENT SERVICES</span></div>
  <div class="contact" style="left:272px;top:439px"><b>A.</b> PO Box 2183,<br>Kestrel Bay QLD 4390<br><b>P.</b> 07 5550 1234<br><b>E.</b> admin@vornal.com.au<br><b>W.</b> vornal.com.au</div>
  <div class="band" style="top:485px" role="img" aria-label="Green to blue chevron road-marking band"></div>
</section>

<!-- Concept 5: gradient bands -->
<section class="sheet sheet--bands">
  <div class="band" style="top:0" role="img" aria-label="Green to blue chevron road-marking band"></div>
  <div class="wordmark" style="left:21px;top:39px"><span class="wordmark__name">VORNAL</span><span class="wordmark__tag">PAVEMENT SERVICES</span></div>
  <div class="letter" style="left:51px;top:86px;width:282px">
    <p>Dear Mrs Halloway,</p>
    <p>The quick, brown fox jumps over a lazy dog. DJs flock by when KTV ax quiz prog. Junk KTV quiz graced by fox whelps. Bawds jog, flick quartz, vex nymphs. Waltz, bad nymph, for quick jigs vex!</p>
    <p>Fox nymphs grab quick-jived waltz. Brick quiz whangs jumpy veldt fox. Bright vixens jump; dozy fowl quack. Quick wafting zephyrs vex bold Jim. Quick zephyrs blow, vexing daft Jim. Fur-clad fop blew my junk TV quiz. How quickly daft jumping zebras vex. Two driven jocks help fax my big quiz. Quick, Baz, get my woven flax jodhpurs! "Now fax quiz Jack!" my brave ghost pled.</p>
    <p>Five quacking zephyrs jolt my wax bed. Flummoxed by job, kvetching W. zaps Iraq. Cozy sphinx waves quart jug of bad milk. A very bad quack might jinx zippy fowls. Few quips galvanized the mock jury box. Quick brown dogs jump over the lazy fox. The jay, pig, fox, zebra, and my wolves quack! Blowzy red vixens fight for a quick jump. Jorund Felwick was gazed by KTV for luck. A wizard's job is to vex chumps quickly in fog. Watch "Quizzard!", Rex Talbot's fun TV quiz game. Woven silk pyjamas exchanged for blue quartz.</p>
    <p>Best Regards,</p>
  </div>
  <div class="band" style="top:485px" role="img" aria-label="Green to blue chevron road-marking band"></div>
</section>

</body>
</html>
```